New document sharing business needs snazzy icons

We need two icons designed for a new document sharing business based in Brisbane, Australia. Users of the website can download high quality document templates and examples, or upload content to share with others.
We need two icons to go on the home page that draws attention to the two main functions of the website (download and share). These icons need to be a little different, but consistent in size and general appearance. These icons will hyperlink to the "download" and "upload" pages of the website.
The first icon needs to have the word "Download" as the dominant word. Under or beside this word the following words need to appear: "search and download documents" in smaller writing. The image needs to portray a professional, elegant look whilst being visually appealing. This icon may use the down arrow or some variation to depict the downloading of a document.
The second icon needs to have the word "Share" as the dominant word. Under or beside this word the following words need to appear: "upload your documents to get free downloads" in smaller writing. This icon may use the up arrow or some variation to depict the sharing or uploading of documents.
I would expect that both icons may use different (but complimentary) colours, and be of the same overall size and structure.
Customers are business managers and executives.
Business
Designer to choose colors to be used in the design.

```html
<!DOCTYPE html>
<html lang="en">
<head>
<meta charset="utf-8">
<title>Download and Share Buttons</title>
<link rel="stylesheet" href="https://fonts.googleapis.com/css2?family=Open+Sans:wght@400&display=swap">
<style>
  :root {
    --bg: #ffffff;
    --red-top: #f36f78;
    --red-mid: #e8303c;
    --red-bottom: #c8182a;
    --red-title: #c92a35;
    --red-icon: #d9202e;
    --blue-top: #86dcf2;
    --blue-mid: #2a9be0;
    --blue-bottom: #1272cf;
    --blue-title: #0d4a78;
    --blue-icon: #3aa0e4;
    --white: #ffffff;
  }
  * { margin: 0; padding: 0; box-sizing: border-box; }
  html, body { width: 1200px; height: 410px; overflow: hidden; background: var(--bg); }
  body { position: relative; font-family: "Open Sans", Arial, sans-serif; }
  .action-button {
    position: absolute; top: 172px; width: 324px; height: 96px;
    border-radius: 10px; overflow: hidden; text-decoration: none;
  }
  .action-button::after {
    content: ""; position: absolute; left: -20px; right: -20px; top: -60px; height: 100px;
    border-radius: 0 0 50% 50% / 0 0 30px 30px;
    background: rgba(255,255,255,0.18);
  }
  .download-button {
    left: 172px;
    background: linear-gradient(to bottom, var(--red-top) 0%, var(--red-top) 38%, var(--red-mid) 45%, var(--red-bottom) 100%);
  }
  .share-button {
    left: 642px;
    background: linear-gradient(to bottom, var(--blue-top) 0%, #7cc9ee 38%, var(--blue-mid) 48%, var(--blue-bottom) 100%);
  }
  .button-title {
    position: absolute; top: 14px; font-size: 48px; line-height: 60px; font-weight: 400; z-index: 1;
  }
  .download-button .button-title { left: 12px; color: var(--red-title); opacity: 0.55; }
  .share-button .button-title { left: 58px; color: var(--blue-title); opacity: 0.8; }
  .button-caption {
    position: absolute; bottom: 8px; color: var(--white); z-index: 2;
  }
  .download-button .button-caption { left: 15px; font-size: 14px; }
  .share-button .button-caption { left: 13px; font-size: 10.5px; bottom: 10px; }
  .button-badge {
    position: absolute; top: 50%; transform: translateY(-50%); z-index: 3;
  }
  .download-button .button-badge { right: 14px; }
  .share-button .button-badge { right: 8px; }
</style>
</head>
<body>
  <a class="action-button download-button" href="#download">
    <span class="button-title">Download</span>
    <span class="button-caption">search and download documents</span>
    <svg class="button-badge" width="60" height="60" viewBox="0 0 60 60" aria-hidden="true">
      <circle cx="30" cy="30" r="29" fill="rgba(255,255,255,0.35)"/>
      <circle cx="30" cy="30" r="26" fill="var(--white)"/>
      <path d="M20 15 H34 L40 21 V45 H20 Z" fill="none" stroke="var(--red-icon)" stroke-width="2"/>
      <path d="M26 20 V34 H22 L30 44 L38 34 H34 V20 Z" fill="var(--red-icon)"/>
    </svg>
  </a>
  <a class="action-button share-button" href="#upload">
    <span class="button-title">Share</span>
    <span class="button-caption">upload your documents to get free downloads</span>
    <svg class="button-badge" width="76" height="76" viewBox="0 0 76 76" aria-hidden="true">
      <circle cx="38" cy="38" r="36" fill="rgba(255,255,255,0.25)"/>
      <circle cx="38" cy="38" r="30" fill="rgba(255,255,255,0.5)"/>
      <circle cx="38" cy="38" r="27" fill="var(--white)"/>
      <path d="M26 23 H44 L50 29 V53 H26 Z" fill="none" stroke="var(--blue-icon)" stroke-width="1.5"/>
      <path d="M31 38 A7 7 0 0 1 43 33" fill="none" stroke="var(--blue-icon)" stroke-width="1.6"/>
      <path d="M45 38 A7 7 0 0 1 33 43" fill="none" stroke="var(--blue-icon)" stroke-width="1.6"/>
      <circle cx="43" cy="33" r="2" fill="var(--blue-icon)"/>
      <circle cx="33" cy="43" r="2" fill="var(--blue-icon)"/>
      <circle cx="31" cy="38" r="1.6" fill="var(--blue-icon)"/>
      <circle cx="45" cy="38" r="1.6" fill="var(--blue-icon)"/>
    </svg>
  </a>
</body>
</html>
```